Website redesign and new logo

Hi we feel that the colours, layout and style along with the logo which is only text at the moment is poor. It seems to lack a quality and luxurious feel and we are about selling high end curtains. The text logo is hard to read as well in my opinion. We are looking for a overall revamp and an new logo. We want to maintain the main parts of the home page but happy to consider any ideas that will improve web traffic. It does not really reflect our achievements either of having curtains recently featured on lumen 6 tv.
The website in question is www.velmorrahangings.co.uk

```html
<!DOCTYPE html>
<html lang="en">
<head>
<meta charset="utf-8">
<title>Velmorra Hangings</title>
<link rel="stylesheet" href="https://fonts.googleapis.com/css2?family=Cinzel:wght@700&family=PT+Sans:wght@400&display=swap">
<style>
:root{
  --teal:#0f7a73;
  --ink:#3e3a36;
  --body:#4a4744;
  --muted:#6f6c69;
  --nav:#4d4b48;
  --page:#f3f1ee;
  --line:#d9d6d2;
  --berry:#a01b4a;
  --band:#efeeec;
  --footer:#2b2b2b;
  --footer-text:#b8b6b3;
  --icon:#8a8886;
}
*{box-sizing:border-box;margin:0;padding:0}
html,body{width:950px;height:1200px;overflow:hidden}
body{position:relative;background:var(--page);font-family:"PT Sans",Arial,sans-serif;color:var(--body)}
.abs{position:absolute}
.top{left:0;top:0;width:950px;height:711px;background:radial-gradient(ellipse at 50% 0%,#ffffff 0%,#f5f3f0 55%,#ecebe8 100%)}
.brand{left:0;top:38px;width:950px;text-align:center;font-family:"Cinzel",Georgia,serif;font-weight:700;color:var(--teal);font-size:26px;letter-spacing:1px;line-height:34px}
.rule{left:90px;top:112px;width:770px;height:1px;background:linear-gradient(90deg,transparent,var(--line) 20%,var(--line) 80%,transparent)}
.nav{left:0;top:131px;width:950px;display:flex;justify-content:center;gap:28px;font-size:13px;line-height:18px;color:var(--nav);text-transform:uppercase}
.nav .on{color:var(--teal)}
.hero{left:80px;top:166px;width:791px;height:347px;background:linear-gradient(90deg,#b79b7c 0%,#e6d3b3 22%,#dfe6e2 42%,#9eb39a 58%,#e6d3b3 78%,#a78f74 100%);box-shadow:0 10px 14px -8px rgba(0,0,0,.45)}
.hero-caption{left:78px;top:466px;width:795px;height:47px;background:rgba(40,36,34,.82);color:#fff;font-family:"Cinzel",Georgia,serif;font-weight:700;font-size:22px;text-align:center;line-height:47px}
.arrow{top:324px;width:32px;height:32px;background:rgba(255,255,255,.85)}
.arrow.prev{left:80px}.arrow.next{left:839px}
.welcome{left:0;top:545px;width:950px;text-align:center;font-family:"Cinzel",Georgia,serif;font-weight:700;color:var(--ink);font-size:26px;line-height:34px}
.welcome-sub{top:580px;font-size:16px;line-height:22px;color:var(--teal)}
.intro{left:100px;top:610px;width:750px;text-align:center;font-size:12.5px;line-height:20px;color:var(--body)}
.btn{left:434px;top:659px;width:82px;height:26px;border-radius:3px;background:linear-gradient(#6a6866,#3f3d3b);color:#fff;font-size:12px;text-align:center;line-height:26px}
.lower{left:0;top:711px;width:950px;height:331px;background:linear-gradient(#f8f8f7,#fbfbfa);border-top:1px solid #e3e1de}
.areas-head{left:87px;top:738px;width:248px;height:39px;background:var(--teal);color:#fff;font-family:"Cinzel",Georgia,serif;font-weight:700;font-size:13px;line-height:39px;text-align:center}
.areas{left:100px;top:789px;width:235px;list-style:none}
.areas li{height:34.7px;font-size:13.5px;color:var(--muted);display:flex;align-items:center}
.areas li .mark{width:28px;font-size:10px;color:#999}
.areas-rule{left:87px;top:1009px;width:248px;height:1px;background:var(--line)}
.video{left:352px;top:739px;width:246px;height:154px;background:linear-gradient(90deg,#6b5645 0%,#d8ccb8 30%,#efe8d8 50%,#d8ccb8 70%,#6b5645 100%);border:1px solid #ddd}
.play{left:451px;top:802px;width:48px;height:33px;border-radius:7px;background:#1e1e1e}
.scatter{left:351px;top:910px;width:90px;font-family:"Cinzel",Georgia,serif;font-weight:700;color:var(--berry);font-size:13px;line-height:21.5px}
.scatter-art{left:434px;top:900px;width:165px;height:104px;background:linear-gradient(180deg,#ffffff 0%,#f2eef2 45%,#c9c2ca 80%,#ffffff 100%)}
.card{left:615px;width:248px;height:77px;background:linear-gradient(#ffffff,#f3f3f2);border:1px solid #dcdad7;display:flex;align-items:center}
.card .ic{width:47px;height:42px;margin:0 18px 0 25px;display:flex;align-items:center;justify-content:center;flex:none}
.card .label{font-family:"Cinzel",Georgia,serif;font-weight:700;color:var(--teal);font-size:15px;line-height:23px}
.contact{left:0;top:1042px;width:950px;height:77px;background:var(--band)}
.c-item{display:flex;align-items:center;gap:10px;font-size:11px;color:var(--muted);line-height:18px}
.footer{left:0;top:1119px;width:950px;height:81px;background:var(--footer)}
.f-links{left:80px;top:1136px;font-size:11px;line-height:16px;color:var(--footer-text)}
.f-links span{margin:0 7px;color:#8a8886}
.copy{left:80px;top:1166px;font-size:10.5px;line-height:16px;color:var(--footer-text)}
.social{top:1149px;width:20px;height:20px;border-radius:50%;background:#5a5957}
</style>
</head>
<body>
<header>
  <div class="abs top"></div>
  <div class="abs brand">VELMORRA HANGINGS</div>
  <div class="abs rule"></div>
  <nav class="abs nav">
    <span class="on">Home</span><span>About Us</span><span>News</span><span>Fabrics</span><span>Scatter Cushions &amp; Bed Throws</span><span>Gallery</span><span>Testimonials</span><span>Contact Us</span>
  </nav>
</header>

<section>
  <div class="abs hero" role="img" aria-label="Bedroom with cream drapes framing a tall window over a city view"></div>
  <div class="abs arrow prev"><svg width="32" height="32"><path d="M20 9 L12 16 L20 23" fill="none" stroke="#555" stroke-width="3"/></svg></div>
  <div class="abs arrow next"><svg width="32" height="32"><path d="M12 9 L20 16 L12 23" fill="none" stroke="#555" stroke-width="3"/></svg></div>
  <div class="abs hero-caption">DOUBLE YOUR HOUSE FOR HALF THE MONEY</div>

  <h1 class="abs welcome">WELCOME TO</h1>
  <h2 class="abs welcome welcome-sub">VELMORRA HANGINGS</h2>
  <p class="abs intro">Hi my name is Maren. Velmorra Hangings is my inspiration. I’m passionate about my fabrics and take pride in what I do. I’ve always enjoyed creating the WOW factor. Designer curtains have never looked so good!</p>
  <div class="abs btn">READ MORE</div>
</section>

<section>
  <div class="abs lower"></div>
  <div class="abs areas-head">THE AREAS WE COVER INCLUDE</div>
  <ul class="abs areas">
    <li><span class="mark">&gt;|</span>CURTAINS BERKSHIRE</li>
    <li><span class="mark">&gt;|</span>CURTAINS BUCKINGHAMSHIRE</li>
    <li><span class="mark">&gt;|</span>CURTAINS OXFORDSHIRE</li>
    <li><span class="mark">&gt;|</span>CURTAINS WINCHESTER</li>
    <li><span class="mark">&gt;|</span>CURTAINS GUILDFORD</li>
    <li><span class="mark">&gt;|</span>CURTAINS OXFORD</li>
  </ul>
  <div class="abs areas-rule"></div>

  <div class="abs video" role="img" aria-label="Video still of patterned curtains drawn back from a window"></div>
  <div class="abs play"><svg width="48" height="33"><path d="M20 11 L30 16.5 L20 22 Z" fill="#fff"/></svg></div>
  <div class="abs scatter">SCATTER CUSHIONS AND BED THROWS</div>
  <div class="abs scatter-art" role="img" aria-label="Lettered banner above a bed dressed with pink cushions"></div>

  <div class="abs card" style="top:738px">
    <div class="ic" role="img" aria-label="Red drape sample" style="background:linear-gradient(90deg,#8e0f12,#d42a22,#8e0f12);border-radius:3px"></div>
    <div class="label">CURTAIN FABRIC<br>TYPES</div>
  </div>
  <div class="abs card" style="top:836px">
    <div class="ic"><svg width="40" height="36"><rect x="1" y="2" width="38" height="32" fill="#f4f4f4" stroke="#c8c8c8"/><rect x="1" y="2" width="38" height="5" fill="#9aa9b8"/><g stroke="#bbb"><line x1="6" y1="12" x2="6" y2="30"/><line x1="13" y1="12" x2="13" y2="30"/><line x1="20" y1="12" x2="20" y2="30"/><line x1="27" y1="12" x2="27" y2="30"/><line x1="34" y1="12" x2="34" y2="30"/></g></svg></div>
    <div class="label">LATEST NEWS</div>
  </div>
  <div class="abs card" style="top:933px">
    <div class="ic"><svg width="44" height="38"><ellipse cx="22" cy="17" rx="20" ry="14" fill="#e7edf5" stroke="#9fb1c7" stroke-width="1.5"/><path d="M12 28 L9 37 L20 30" fill="#e7edf5" stroke="#9fb1c7" stroke-width="1.5"/></svg></div>
    <div class="label">OUR CUSTOMERS<br>TESTIMONIALS</div>
  </div>
</section>

<section>
  <div class="abs contact"></div>
  <div class="abs c-item" style="left:121px;top:1063px">
    <svg width="20" height="22"><rect x="1" y="1" width="18" height="20" fill="none" stroke="#8a8886" stroke-width="1.5"/><rect x="8" y="8" width="4" height="13" fill="#8a8886"/></svg>
    <span>14 Harrow Lane,<br>Elmbury, Westshire, EB4 2QT</span>
  </div>
  <div class="abs c-item" style="left:380px;top:1071px">
    <svg width="22" height="22"><path d="M3 3 Q1 10 8 16 Q14 21 20 19 L20 15 L15 13 L12 15 Q7 12 6 8 L8 5 L6 1 Z" fill="#8a8886"/></svg>
    <span>Phone: 0300 555 0182</span>
  </div>
  <div class="abs c-item" style="left:624px;top:1068px">
    <svg width="21" height="16"><rect x="1" y="1" width="19" height="14" fill="#8a8886"/><path d="M1 1 L10.5 9 L20 1" fill="none" stroke="#efeeec" stroke-width="1.5"/></svg>
    <span>E-mail : info@velmorrahangings.co.uk</span>
  </div>
</section>

<footer>
  <div class="abs footer"></div>
  <div class="abs f-links">Home<span>|</span>About Us<span>|</span>News<span>|</span>Fabrics<span>|</span>Scatter Cushions &amp; Bed Throws<span>|</span>Gallery<span>|</span>Testimonials<span>|</span>Contact us</div>
  <div class="abs copy">Copyright &copy; 2013 &nbsp;Velmorra Hangings. &nbsp;All rights reserved.</div>
  <div class="abs social" style="left:768px"></div>
  <div class="abs social" style="left:795px"></div>
  <div class="abs social" style="left:823px"></div>
  <div class="abs social" style="left:851px"></div>
</footer>
</body>
</html>
```